Norwegian Mobile Home/Cabin Producer Needs Brochure Design

We make and deliver our own brand of mobile homes especially made for Norway and it's weather conditions. We differ from other brands in building quality in regards to a much more solid construction, insulation and choices. We work with our customer from the beginning and build them after their demands and wishes.
We need a brochure that holds us out as top of the line. We deliver mobile homes of all kinds and sizes. Both to the private and professional sector.
For the professional sector, mainly camping sites we want to show, lodges-, sanitary- and kitchen wagoons etc.
So we need a brochure of 14-20 pages in A4 where the double pages can be printed in A3 format.
We have logo (provided). But we need cover as well as back suggestions.
It should start with pages where we can teel who we are and stand for.Piicture(s) and space for some editable text (which we can write in norwegian). The text part can have a transparent background......or not. Give us your best shot. Also a smaller part in the private sector that shows winter time.
We want other pages for the private sector that shows what we deliver and the possibilities of choices.
Pages for the the professional sector.
Pages that show our production. How we transport. And the split construction. Only pictures from this portfolio here. (see fotoskap portfolios)
Take a look at provided pictures and our website www.solvikhytta.no for inspiration.
Here's a FotoSkap link to Pictures to choose from. http://bildelagr.example/K4TQ9P
(Hope it Works, let me know if not)
Our company name in small letters "fjordgrønn hyttebygg" means directly translated "fjordgreen cabin builds".
Looking forward to your suggestions.
Target Market(s)
Private market for vacation mobile homes. Camping sites and similar
Industry/Entity Type
Insulation
Requirements
Must have
- Our logo on the front page. Simple but inviting and professional
Logo and address on the back.

```html
<!DOCTYPE html>
<html lang="no">
<head>
<meta charset="utf-8">
<title>fjordgrønn hyttebygg – brosjyre</title>
<link rel="stylesheet" href="https://fonts.googleapis.com/css2?family=Cormorant+Garamond:wght@400;600&family=Pinyon+Script&display=swap">
<style>
  :root {
    --backdrop: #dcdcd8;
    --sky: #7f97bf;
    --sky-dark: #6c84ad;
    --paper: #f3f1ee;
    --page-grey: #e4e3e1;
    --taupe: #8a7565;
    --taupe-light: #b7a392;
    --sand: #d9c7b2;
    --white: #ffffff;
    --ink: #3d3a37;
    --serif: "Cormorant Garamond", Georgia, serif;
    --script: "Pinyon Script", cursive;
  }
  * { box-sizing: border-box; margin: 0; padding: 0; }
  html, body { width: 1200px; height: 900px; overflow: hidden; }
  body { background: var(--backdrop); font-family: var(--serif); color: var(--ink); position: relative; }

  .spread { position: absolute; width: 540px; height: 380px; display: flex; box-shadow: 0 6px 18px rgba(0,0,0,.18); }
  .spread--cover { left: 50px; top: 45px; }
  .spread--rooms { left: 610px; top: 45px; }
  .spread--options { left: 330px; top: 470px; }
  .page { position: relative; width: 270px; height: 380px; overflow: hidden; }
  .page + .page { border-left: 1px solid rgba(0,0,0,.12); }

  /* cover */
  .back-cover { background: var(--sky); color: var(--white); }
  .back-cover__name { position: absolute; top: 170px; width: 100%; text-align: center; font-size: 17px; letter-spacing: .5px; }
  .back-cover__address { position: absolute; bottom: 22px; width: 100%; text-align: center; font-size: 8px; line-height: 1.4; }
  .front-cover { background: var(--sky); }
  .front-cover__photo { position: absolute; left: 0; top: 0; width: 236px; height: 380px; background: linear-gradient(160deg, #f1ece4 0%, #d8cbbb 55%, #a98d70 100%); }
  .front-cover__tagline { position: absolute; left: 0; top: 0; width: 236px; height: 92px; background: rgba(255,255,255,.55); font-family: var(--script); font-size: 30px; line-height: 1.05; color: var(--white); text-shadow: 0 0 2px rgba(0,0,0,.25); padding: 10px 14px 0 40px; }
  .front-cover__tagline span { display: block; padding-left: 60px; }
  .front-cover__name { position: absolute; right: 6px; bottom: 16px; writing-mode: vertical-rl; transform: rotate(180deg); color: var(--white); font-size: 19px; }

  /* room photo spread */
  .text-band { position: absolute; left: 0; top: 0; width: 100%; height: 120px; }
  .text-band--sky { background: var(--sky); }
  .text-band--sand { background: var(--sand); }
  .text-column { position: absolute; top: 8px; width: 118px; color: var(--white); font-size: 10px; line-height: 1.2; text-align: justify; }
  .photo { position: absolute; left: 0; width: 100%; }
  .photo--garden { top: 120px; height: 260px; background: linear-gradient(180deg, #6f8a4c 0%, #dfe3e2 45%, #4f6a33 100%); }
  .photo--bedroom { top: 120px; height: 260px; background: linear-gradient(150deg, #e9dccb 0%, #c7ab94 50%, #8e6d5c 100%); }
  .page-number { position: absolute; bottom: 6px; width: 8px; height: 8px; border-radius: 50%; background: var(--white); }

  /* options spread */
  .options-page { background: var(--page-grey); }
  .options-page__head { position: absolute; left: 0; top: 0; width: 100%; height: 34px; background: var(--sky); color: var(--white); font-size: 12px; padding: 9px 0 0 40px; }
  .panel { position: absolute; background: var(--taupe); color: var(--white); border-radius: 6px; padding: 6px 8px; font-size: 9px; }
  .panel__title { font-family: var(--script); font-size: 15px; margin-bottom: 4px; }
  .swatch { position: absolute; width: 52px; height: 52px; border-radius: 50%; border: 2px solid var(--taupe); }
  .swatch--wood { left: 168px; top: 42px; background: radial-gradient(circle, #9a5a33, #5d3420); }
  .swatch--colours { left: 44px; top: 242px; background: linear-gradient(180deg, #c9b27a, #8e3b2c 50%, #5a6b3a); }
  .spec-table { position: absolute; border-collapse: collapse; font-size: 8px; background: var(--white); }
  .spec-table caption { background: var(--taupe-light); color: var(--white); font-family: var(--script); font-size: 14px; padding: 2px 0; border-radius: 5px 5px 0 0; }
  .spec-table th { background: var(--sky); color: var(--white); font-weight: 600; padding: 3px 5px; }
  .spec-table td { border: 1px solid #b9b6b2; padding: 3px 5px; text-align: center; }
  .spec-table td:first-child { background: var(--sky-dark); color: var(--white); text-align: left; }
  .winter-page { background: var(--sky); }
  .photo--winter { top: 112px; height: 220px; background: linear-gradient(180deg, #c9ccd2 0%, #8d9096 35%, #a3473f 48%, #eef0f2 62%, #ffffff 100%); }
</style>
</head>
<body>

<section class="spread spread--cover">
  <div class="page back-cover">
    <p class="back-cover__name">fjordgrønn hyttebygg as</p>
    <p class="back-cover__address">Postboks 120<br>4630 Sørvik</p>
  </div>
  <div class="page front-cover">
    <div class="front-cover__photo" role="img" aria-label="Bright living room interior with white furniture and wooden floor"></div>
    <p class="front-cover__tagline">Functional<span>Elegance</span></p>
    <p class="front-cover__name">fjordgrønn hyttebygg as</p>
  </div>
</section>

<section class="spread spread--rooms">
  <div class="page">
    <div class="text-band text-band--sky"></div>
    <p class="text-column" style="left:126px">Vi bygger hytter for norsk vær, med solid konstruksjon, tykk isolasjon og fri planløsning. Hver modell lages etter dine ønsker.</p>
    <div class="photo photo--garden" role="img" aria-label="White mobile home with veranda in a green garden"></div>
    <span class="page-number" style="left:8px"></span>
  </div>
  <div class="page">
    <div class="text-band text-band--sand"></div>
    <p class="text-column" style="left:96px">Lyse rom, varme materialer og gjennomtenkte detaljer gir en hytte du trives i hele året, sommer som vinter.</p>
    <div class="photo photo--bedroom" role="img" aria-label="Cosy bedroom with cushions and a window"></div>
    <span class="page-number" style="left:6px"></span>
  </div>
</section>

<section class="spread spread--options">
  <div class="page options-page">
    <p class="options-page__head">Velg detaljer etter egen smak</p>
    <div class="panel" style="left:34px;top:44px;width:120px;height:62px">
      <p class="panel__title">Lakkering</p>
      <p>Hvit, grå, beige eller brun</p>
    </div>
    <div class="swatch swatch--wood" role="img" aria-label="Wood stain sample"></div>
    <table class="spec-table" style="left:44px;top:116px;width:212px">
      <caption>Valg</caption>
      <tr><th>Modell</th><th>Lengde</th><th>Bredde</th><th>Pris</th></tr>
      <tr><td>Standard</td><td>9 m</td><td>3,5 m</td><td>—</td></tr>
      <tr><td>Komfort</td><td>11 m</td><td>3,7 m</td><td>—</td></tr>
      <tr><td>Premium</td><td>12 m</td><td>4 m</td><td>—</td></tr>
    </table>
    <div class="swatch swatch--colours" role="img" aria-label="Colour chart sample"></div>
    <div class="panel" style="left:152px;top:232px;width:104px;height:54px">
      <p class="panel__title">Fargekart</p>
      <p>Se fargene i kartet</p>
    </div>
    <table class="spec-table" style="left:44px;top:300px;width:212px">
      <tr><th>Modell</th><th>Lengde</th><th>Bredde</th><th>Pris</th></tr>
      <tr><td>Terrasse</td><td>4 m</td><td>2 m</td><td>—</td></tr>
      <tr><td>Veranda</td><td>6 m</td><td>2,5 m</td><td>—</td></tr>
    </table>
    <span class="page-number" style="right:6px;background:var(--sky)"></span>
  </div>
  <div class="page winter-page">
    <p class="text-column" style="left:46px;width:170px">Vinterklar fra fabrikk: forsterket tak, doble vinduer og gulvvarme holder kulden ute når snøen legger seg over fjellet.</p>
    <div class="photo photo--winter" role="img" aria-label="Red cabin in a snowy landscape with mountains"></div>
  </div>
</section>

</body>
</html>
```